Stationery Design Project - Mark Delaveri

I have recently designed my personal logo - Mark Delaveri (here on pixelhive.com) and now i'm looking to complete my corporate identity, with adding:
- Business Card
- Letter Head
- Envelope
- Brochure template (that will be used to promote any of the workshops or other services I provide along with a short summary about my credentials, and testimonials) - you can take your pick from the website: http://markdelaveri.com

Refer to website for more insight into the brand and the look & feel

PS.
- PLEASE REFER TO ATTACHED FILE AND READ THE "SHOULD NOT HAVE SECTION OF THIS BRIEF"
- I have attached two vector files, displaying the logo alteration on two different backgrounds (dark & light)
Updates

ONLY 2 DAYS LEFT ON DEADLINE. KEEP THOSE DESIGNS COMING.

Target Market(s)

1) One-on-one Business Executive 2) Companies requesting my workshops for mid management teams & public speaking events like BRIM Forums

Industry/Entity Type

Business

Requirements
Must have
• - must fit the look and feel of the logo (notice that I have attached the logo, and an emblem)
- the final files should be ready for printing - with info on colours, sizes, bleed area, margins, UV spot (if applicable), suggested material to print on (applies to business cards in particular)
- brand guide lines should be laid out too (font, colour, etc ...)
Nice to have
• It would be nice to produce something different that your standard sizes & di-cut in terms of business card, and letter head ...
Should not have
• THE EMBLEM (MD) AND THE LOGO (MARK DELAVERI) SHOULD NOT BE LAYED OUT AS PER THE ATTACHED FILE - THEY SHOULD BE SEPARATED - THE EMBLEM (MD) CAN BE USED IN PARTIAL OR AS WATERMARK - BUT NOT THE LOGO (MARK DELAVERI)

```html
<!DOCTYPE html>
<html lang="en">
<head>
<meta charset="utf-8">
<title>Mark Delaveri – Business Card</title>
<link rel="stylesheet" href="https://fonts.googleapis.com/css2?family=Oswald:wght@600&family=Open+Sans:wght@400;700&display=swap">
<style>
  :root {
    --page: #e9e7e4;
    --card-white: #ffffff;
    --card-grey: #58595b;
    --card-grey-dark: #4a4b4d;
    --brand-grey: #5f6062;
    --brand-blue: #2ec4f0;
    --text-light: #ffffff;
    --text-muted: #6d6e70;
  }
  * { box-sizing: border-box; margin: 0; padding: 0; }
  html, body { width: 1200px; height: 758px; overflow: hidden; }
  body {
    background: var(--page);
    font-family: "Open Sans", Arial, sans-serif;
    position: relative;
  }
  .card {
    position: absolute;
    top: 224px;
    width: 520px;
    height: 310px;
    clip-path: polygon(14px 0, 480px 0, 520px 40px, 520px 296px, 506px 310px, 40px 310px, 0 270px, 0 14px);
    filter: drop-shadow(0 6px 10px rgba(0,0,0,.18));
  }
  .card-front { left: 60px; background: var(--card-white); }
  .card-back {
    left: 620px;
    background: linear-gradient(135deg, var(--card-grey-dark), var(--card-grey));
  }
  .card-front .swoosh { position: absolute; inset: 0; width: 100%; height: 100%; }

  .wordmark {
    position: absolute;
    left: 40px; top: 28px;
    font-family: "Oswald", "Arial Narrow", sans-serif;
    font-weight: 600;
    font-size: 56px;
    line-height: 1;
    letter-spacing: -1px;
    color: var(--brand-grey);
  }
  .wordmark-rule {
    position: absolute;
    left: 40px; top: 96px;
    width: 380px; height: 2px;
    background: var(--brand-blue);
  }
  .tagline {
    position: absolute;
    left: 170px; top: 100px;
    font-size: 10px;
    font-weight: 700;
    letter-spacing: .5px;
    color: var(--brand-blue);
  }
  .address {
    position: absolute;
    left: 110px; top: 128px;
    font-size: 13px;
    letter-spacing: 1px;
    color: var(--text-muted);
  }
  .holder {
    position: absolute;
    right: 300px; top: 236px;
    text-align: right;
    color: var(--text-light);
    line-height: 1.25;
  }
  .holder-name { font-weight: 700; font-size: 16px; }
  .holder-title { font-size: 16px; }
  .divider {
    position: absolute;
    left: 230px; top: 226px;
    width: 1px; height: 62px;
    background: rgba(255,255,255,.6);
  }
  .contacts {
    position: absolute;
    left: 240px; top: 222px;
    list-style: none;
    color: var(--text-light);
    font-size: 12.5px;
    line-height: 17px;
  }
  .contacts li { display: flex; align-items: center; gap: 6px; }
  .contacts svg { width: 10px; height: 10px; fill: var(--text-light); flex: none; }

  .emblem {
    position: absolute;
    left: 190px; top: 54px;
    width: 140px; height: 140px;
    border: 8px solid var(--text-light);
    border-radius: 50%;
    display: flex; align-items: center; justify-content: center;
    font-family: "Open Sans", Arial, sans-serif;
    font-weight: 700;
    font-size: 50px;
    color: var(--text-light);
  }
  .back-url {
    position: absolute;
    left: 0; right: 0; top: 228px;
    text-align: center;
    font-size: 19px;
    letter-spacing: 3px;
    color: var(--text-light);
  }
</style>
</head>
<body>
  <section class="card card-front" aria-label="Business card front">
    <svg class="swoosh" viewBox="0 0 520 310" preserveAspectRatio="none" aria-hidden="true">
      <path d="M0 180 Q300 196 520 126 L520 144 Q300 218 0 206 Z" fill="var(--brand-blue)"/>
      <path d="M0 202 Q300 214 520 142 L520 310 L0 310 Z" fill="var(--card-grey)"/>
    </svg>
    <div class="wordmark">MARK DELAVERI</div>
    <div class="wordmark-rule"></div>
    <div class="tagline">LEAD WITH PURPOSE EVERY DAY</div>
    <p class="address">00, Complex name, Street, city 002</p>

    <div class="holder">
      <div class="holder-name">Your Name</div>
      <div class="holder-title">Title</div>
    </div>
    <div class="divider"></div>
    <ul class="contacts">
      <li><svg viewBox="0 0 10 10"><rect x="2.5" y="0" width="5" height="10" rx="1"/></svg>+123-456-789</li>
      <li><svg viewBox="0 0 10 10"><circle cx="5" cy="3" r="2.6"/><path d="M0 10 Q5 3 10 10 Z"/></svg>+123-456-789</li>
      <li><svg viewBox="0 0 10 10"><rect x="0" y="2" width="10" height="7"/></svg>info@markdelaveri.com</li>
      <li><svg viewBox="0 0 10 10"><circle cx="5" cy="5" r="4.5"/></svg>www.markdelaveri.com</li>
    </ul>
  </section>

  <section class="card card-back" aria-label="Business card back">
    <div class="emblem">MD</div>
    <p class="back-url">www.markdelaveri.com</p>
  </section>
</body>
</html>
```